Antibacterial Hand Wash Squeeze Tube Label

We're looking for a contemporary label design for a new Antibacterial Hand Wash for an 8oz squeeze tube. The new consumer brand will be sold to consumers in major US retail stores & online. The moisturizing hand wash contains Aloe Vera, vitamin E, and other natural ingredients so the design should include the color green. Real photos are very effective on packaging, so a picture of Aloe Vera or possibly two hands washing would help draw consumers' attention to the tube on the retail shelf. The front label may wrap around the sides. Rear must be left mostly blank
US Consumers - retail stores & online
Consumer

```html
<!DOCTYPE html>
<html lang="en">
<head>
<meta charset="utf-8">
<title>Valoren Anti Bacterial Hand Wash – Tube Label</title>
<link rel="stylesheet" href="https://fonts.googleapis.com/css2?family=Bebas+Neue&family=Arimo:wght@400;700&display=swap">
<style>
  :root {
    --paper: #ffffff;
    --page: #eeeeee;
    --navy: #1a2a86;
    --navy-deep: #14216f;
    --brand-red: #e0231c;
    --leaf-green: #27b24a;
    --ink: #1a1a1a;
    --white: #ffffff;
  }
  * { margin: 0; padding: 0; box-sizing: border-box; }
  html, body {
    width: 900px;
    height: 1200px;
    overflow: hidden;
    background: var(--page);
  }
  .label {
    position: relative;
    width: 900px;
    height: 1200px;
    background: var(--paper);
    font-family: "Arimo", Arial, sans-serif;
    color: var(--ink);
    text-align: center;
  }
  .brand-name {
    position: absolute;
    top: 150px;
    left: 0;
    width: 100%;
    font-size: 40px;
    font-weight: 400;
    letter-spacing: 1px;
    color: var(--brand-red);
  }
  .product-title {
    position: absolute;
    top: 240px;
    left: 0;
    width: 100%;
    font-family: "Bebas Neue", "Oswald", sans-serif;
    font-weight: 400;
    font-size: 118px;
    line-height: 0.86;
    color: var(--navy);
  }
  .claim {
    position: absolute;
    top: 558px;
    left: 250px;
    width: 400px;
    font-size: 25px;
    line-height: 1.2;
    color: var(--ink);
  }
  .strength-pill {
    position: absolute;
    top: 644px;
    left: 50%;
    transform: translateX(-50%);
    padding: 7px 34px;
    background: var(--navy);
    color: var(--white);
    font-size: 25px;
    border-radius: 30px;
    white-space: nowrap;
  }
  .color-band {
    position: absolute;
    top: 712px;
    left: 0;
    width: 100%;
    height: 488px;
    background: var(--navy);
  }
  .care-icon {
    position: absolute;
    top: 736px;
    left: 50%;
    transform: translateX(-50%);
    width: 150px;
    height: 170px;
  }
  .hand-mark {
    position: absolute;
    top: 852px;
    left: 50%;
    transform: translateX(-50%);
    width: 150px;
    height: 56px;
    border-radius: 28px;
    background: var(--navy-deep);
  }
  .benefits {
    position: absolute;
    top: 950px;
    left: 330px;
    list-style: none;
    text-align: left;
    color: var(--leaf-green);
    font-size: 27px;
    line-height: 1.12;
  }
  .benefits li { margin-bottom: 14px; padding-left: 26px; position: relative; }
  .benefits li::before {
    content: "✓";
    position: absolute;
    left: 0;
    font-size: 22px;
  }
  .net-volume {
    position: absolute;
    top: 1130px;
    left: 0;
    width: 100%;
    font-size: 34px;
    color: var(--white);
  }
</style>
</head>
<body>
  <main class="label">
    <div class="brand-name">VALOREN</div>
    <h1 class="product-title">Anti<br>Bacterial<br>Hand Wash</h1>
    <p class="claim">Kills 99.9 % of germs and bacteria</p>
    <div class="strength-pill">Maximum Strength</div>

    <section class="color-band">
    </section>

    <svg class="care-icon" viewBox="0 0 150 170" aria-hidden="true">
      <circle cx="75" cy="52" r="44" fill="none" stroke="var(--white)" stroke-width="5"/>
      <rect x="66" y="30" width="18" height="44" rx="3" fill="var(--white)"/>
      <rect x="53" y="43" width="44" height="18" rx="3" fill="var(--white)"/>
    </svg>
    <div class="hand-mark" role="img" aria-label="Line icon of an open hand beneath the care symbol"></div>

    <ul class="benefits">
      <li>Moisturizing</li>
      <li>With Aloe Vera &amp;<br>Vitamin E</li>
      <li>Other natural<br>ingredients</li>
    </ul>

    <div class="net-volume">8 fl. oz</div>
  </main>
</body>
</html>
```